Professional business cards for real estate development company

I need business cards for my new real estate development company. The company, "LUMAR" is a real estate development, investment, and advisory firm with a focus on multifamily, office, and mixed-use projects across primary and secondary markets in the Southeast United States.

Style preference is modern

Industry/Entity Type

Real Estate Development

Contact Information for Business Card

The business cards need to include:
Name
Title
Mailing Address
Phone Number
Web Address

Logo is attached. I would like white to be the primary color with incorporation of the company colors: #232D3A and #B5A451

Font styles to use
Other font styles liked:
• Montserrat, Avenir

Requirements
Must have
• Company Logo. No need to include the company name since the name is in the logo.
Should not have
• No line type designs

```html
<!DOCTYPE html>
<html lang="en">
<head>
<meta charset="UTF-8">
<title>LUMAR Business Card</title>
<link href="https://fonts.googleapis.com/css2?family=Montserrat:wght@500;600;700&display=swap" rel="stylesheet">
<style>
  :root {
    --navy: #232D3A;
    --navy-light: #3a4656;
    --gold: #B5A451;
    --white: #ffffff;
    --stage: #e6e6e6;
    --ink: #232D3A;
  }
  * { box-sizing: border-box; margin: 0; padding: 0; }
  html, body {
    width: 1200px; height: 982px; overflow: hidden;
    background: var(--stage);
    font-family: "Montserrat", sans-serif;
  }
  .sheet {
    position: relative; width: 1200px; height: 982px;
    display: flex; justify-content: center; align-items: center; gap: 64px;
  }
  .card {
    position: relative; width: 340px; height: 580px; overflow: hidden;
    box-shadow: 0 6px 18px rgba(0,0,0,0.18);
  }
  /* Front */
  .card--front { background: var(--white); }
  .brand {
    position: absolute; left: 0; right: 0; top: 118px;
    display: flex; justify-content: center; align-items: center; gap: 12px;
  }
  .brand__mark { width: 18px; height: 18px; background: var(--navy); }
  .brand__name {
    font-size: 44px; font-weight: 600; letter-spacing: 4px; color: var(--navy);
  }
  .card--back .brand { top: 240px; }
  .card--back .brand__mark { background: var(--white); }
  .card--back .brand__name { color: var(--white); }

  .person { position: absolute; left: 0; right: 0; top: 262px; text-align: center; }
  .person__name { font-size: 25px; font-weight: 700; color: var(--gold); letter-spacing: 0.5px; }
  .person__title { font-size: 13px; font-weight: 600; color: var(--ink); letter-spacing: 0.6px; margin-top: 2px; }

  .divider { position: absolute; left: 60px; top: 338px; width: 220px; height: 26px; }

  .contact { position: absolute; left: 0; right: 0; top: 374px; text-align: center; }
  .contact__line { font-size: 13.5px; font-weight: 500; color: var(--ink); line-height: 22px; }

  .address-band {
    position: absolute; left: 0; right: 0; bottom: 0; height: 132px;
    background: var(--navy); text-align: center; padding-top: 40px;
  }
  .address-band__pin { position: absolute; left: 157px; top: -13px; width: 26px; height: 28px; }
  .address-band__line { font-size: 13px; font-weight: 500; color: var(--white); line-height: 19px; }

  /* Back */
  .card--back {
    background: radial-gradient(ellipse at 55% 48%, var(--navy-light) 0%, var(--navy) 60%);
  }
  .back-web {
    position: absolute; left: 0; right: 0; bottom: 62px; text-align: center;
    font-size: 14px; font-weight: 500; color: var(--gold); letter-spacing: 0.3px;
  }
</style>
</head>
<body>
<main class="sheet">
  <section class="card card--front">
    <div class="brand"><span class="brand__mark"></span><span class="brand__name">LUMAR</span></div>

    <div class="person">
      <p class="person__name">DANIEL REYES</p>
      <p class="person__title">MANAGING DIRECTOR</p>
    </div>

    <svg class="divider" viewBox="0 0 220 26" aria-hidden="true">
      <line x1="0" y1="13" x2="220" y2="13" stroke="#B5A451" stroke-width="1.5"/>
      <g fill="#B5A451">
        <polygon points="80,4 88,8.5 88,17.5 80,22 72,17.5 72,8.5"/>
        <polygon points="110,4 118,8.5 118,17.5 110,22 102,17.5 102,8.5"/>
        <polygon points="140,4 148,8.5 148,17.5 140,22 132,17.5 132,8.5"/>
      </g>
      <g fill="none" stroke="#fff" stroke-width="1.2">
        <path d="M77 10 q0 6 6 6"/>
        <rect x="105.5" y="10" width="9" height="6"/>
        <path d="M105.5 10 l4.5 3.5 l4.5 -3.5"/>
        <circle cx="140" cy="13" r="4"/>
        <line x1="136" y1="13" x2="144" y2="13"/>
      </g>
    </svg>

    <div class="contact">
      <p class="contact__line">404-555-0187</p>
      <p class="contact__line">hello@lumarco.com</p>
      <p class="contact__line">www.lumarco.com</p>
    </div>

    <div class="address-band">
      <svg class="address-band__pin" viewBox="0 0 26 28" aria-hidden="true">
        <polygon points="13,0 26,7 26,21 13,28 0,21 0,7" fill="#B5A451"/>
        <path d="M13 8 a4 4 0 0 1 4 4 c0 3 -4 7 -4 7 s-4 -4 -4 -7 a4 4 0 0 1 4 -4z" fill="#fff"/>
        <circle cx="13" cy="12" r="1.4" fill="#B5A451"/>
      </svg>
      <p class="address-band__line">1200 Peachtree Street NE,</p>
      <p class="address-band__line">Atlanta, GA - 30309</p>
    </div>
  </section>

  <section class="card card--back">
    <div class="brand"><span class="brand__mark"></span><span class="brand__name">LUMAR</span></div>
    <p class="back-web">www.lumarco.com</p>
  </section>
</main>
</body>
</html>
```